Branding Postcard for Real Estate Brokerage

I am a Real Estate Broker looking for a template postcard that I can use with lots of types of situations , solds, listed property, etc but has a standard layout that is consistent so it will be recognizable and tied to me. There was one that was on the template group that caught my eye. I was thinking of using the A in my logo as the script or watermark. I have uploaded my idea on that as well as other logos, etc. My goal is to have a template that I can add text to and market different things / sales / request action for pricing, etc.

Target Market(s)

Homeowners in Neighborhoods where I have sold homes

Industry/Entity Type

Real Estate

Requirements
Must have
• Area to add label for mailing, Area in front has to be a template where I can write specifics of the mailing, Consistent branding

```html
<!DOCTYPE html>
<html lang="en">
<head>
<meta charset="utf-8">
<title>Harborline Real Estate Brokerage – Postcard</title>
<link rel="stylesheet" href="https://fonts.googleapis.com/css2?family=Montserrat:wght@800&family=Lato:wght@400;700&family=PT+Serif&display=swap">
<style>
  :root {
    --navy: #26348a;
    --navy-dark: #1b2670;
    --lavender-top: #d3d6ec;
    --lavender-bottom: #9ba2d2;
    --ink: #1f1f2a;
    --brand-ink: #2a2f6e;
    --paper: #ffffff;
    --grey-light: #f1f1f1;
    --grey-mid: #c9c9c9;
    --backdrop: #202022;
  }
  * { box-sizing: border-box; margin: 0; padding: 0; }
  html, body { width: 902px; height: 1200px; overflow: hidden; }
  body { background: var(--backdrop); position: relative; font-family: "Lato", sans-serif; color: var(--ink); }

  .card { position: absolute; box-shadow: 0 6px 16px rgba(0,0,0,.55); overflow: hidden; }

  /* ---------- Front ---------- */
  .front { left: 100px; top: 30px; width: 722px; height: 556px;
    background: linear-gradient(180deg, var(--lavender-top), var(--lavender-bottom)); }
  .front .headline-band { position: absolute; left: 0; top: 32px; width: 480px; height: 86px; background: var(--navy); }
  .front .headline { position: absolute; left: 22px; top: 38px; font-family: "Montserrat", sans-serif; font-weight: 800;
    font-size: 66px; letter-spacing: 1px; color: var(--paper); text-shadow: 0 2px 3px rgba(0,0,0,.45); line-height: 74px; }

  .brand-box { position: absolute; background: linear-gradient(180deg, #ffffff, #e6e6ea);
    box-shadow: 0 2px 5px rgba(0,0,0,.35); display: flex; align-items: center; justify-content: center; gap: 10px; }
  .brand-mark { width: 14px; height: 14px; background: var(--brand-ink); flex: none; }
  .brand-name { font-family: "Lato", sans-serif; font-weight: 400; color: var(--brand-ink); line-height: 1.15; }
  .brand-name span { display: block; }
  .brand-name .big { font-size: 24px; }
  .brand-name .small { font-size: 14px; }
  .front .brand-box { left: 472px; top: 24px; width: 228px; height: 96px; }

  .tab { position: absolute; background: var(--navy); color: var(--paper); font-family: "Lato", sans-serif;
    font-weight: 700; font-size: 18px; line-height: 27px; padding-left: 20px; }
  .front .offer-tab { left: 5px; top: 140px; width: 172px; height: 27px; }
  .front .contact-tab { left: 5px; top: 418px; width: 132px; height: 27px; }

  .offer-text { position: absolute; left: 26px; top: 175px; width: 354px; font-family: "PT Serif", serif;
    font-size: 13.4px; line-height: 19.3px; text-align: justify; color: var(--ink); }

  .photo { position: absolute; border: 3px solid var(--paper); box-shadow: 0 2px 6px rgba(0,0,0,.4); }
  .photo-terrace { left: 410px; top: 152px; width: 288px; height: 166px;
    background: linear-gradient(180deg, #6f9bd8 0%, #9bb6d6 40%, #8a6d55 70%, #6e5441 100%); }
  .photo-house { left: 410px; top: 342px; width: 288px; height: 168px;
    background: linear-gradient(180deg, #5b8fd9 0%, #a9c3e4 35%, #d8c9a0 55%, #5d7d3c 80%, #7a8d4c 100%); }

  .contact-list { position: absolute; left: 18px; list-style: none; font-size: 14px; color: var(--ink); }
  .contact-list li { display: flex; align-items: center; gap: 8px; height: 25.5px; }
  .contact-list svg { width: 12px; height: 12px; fill: var(--navy); flex: none; }
  .front .contact-list { top: 448px; }

  .front .footer-band { position: absolute; left: 0; top: 526px; width: 100%; height: 30px; background: var(--navy); }

  /* ---------- Back ---------- */
  .back { left: 105px; top: 615px; width: 715px; height: 563px; background: var(--paper); }
  .back .title-band { position: absolute; left: 0; top: 23px; width: 470px; height: 70px; background: var(--navy); }
  .back .title { position: absolute; left: 270px; top: 42px; font-family: "Montserrat", sans-serif; font-weight: 800;
    font-size: 27px; color: var(--paper); text-shadow: 0 2px 3px rgba(0,0,0,.45); }
  .back .brand-box { left: 468px; top: 13px; width: 232px; height: 92px; }

  .portrait-frame { position: absolute; left: 17px; top: 33px; width: 172px; height: 210px; background: var(--paper);
    padding: 9px; box-shadow: 0 3px 8px rgba(0,0,0,.45); transform: rotate(-2deg); }
  .portrait { width: 100%; height: 100%; background: linear-gradient(180deg, #6b4d3a 0%, #4a3427 55%, #1e1e22 100%); }

  .agent-name { position: absolute; left: 203px; top: 102px; font-family: "Lato", sans-serif; font-weight: 700;
    font-size: 22px; letter-spacing: .5px; color: var(--navy); }
  .back .contact-list { top: 130px; left: 203px; font-size: 14px; font-weight: 700; }
  .back .contact-list li { height: 23px; }
  .blog-label { position: absolute; left: 203px; top: 212px; font-weight: 700; font-size: 14.5px; color: var(--navy); }
  .blog-url { position: absolute; left: 203px; top: 235px; font-family: "PT Serif", serif; font-weight: 700; font-size: 11.5px; }

  .bio { position: absolute; left: 0; top: 263px; width: 465px; height: 300px; padding: 20px 12px 0 20px;
    background: linear-gradient(90deg, var(--grey-light) 0%, #e2e2e2 60%, var(--grey-mid) 100%);
    font-size: 14px; line-height: 17.5px; text-align: justify; color: var(--ink); }
  .bio p { margin-bottom: 9px; }

  .stamp-box { position: absolute; left: 632px; top: 152px; width: 64px; height: 75px; border: 2px solid #111; }
  .address-line { position: absolute; left: 507px; width: 188px; height: 2px; background: #222; }
</style>
</head>
<body>

<section class="card front">
  <div class="headline-band"></div>
  <h1 class="headline">JUST SOLD</h1>
  <div class="brand-box">
    <div class="brand-mark"></div>
    <div class="brand-name"><span class="big">Harborline</span><span class="small">Real Estate Brokerage</span></div>
  </div>

  <div class="tab offer-tab">Special Offer</div>
  <p class="offer-text">Lorem ipsum dolor sit amet, consectetuer adipiscing elit, sed diam nonummy nibh euismod tincidunt ut laoreet dolore magna aliquam erat volutpat. Ut wisi enim ad minim veniam, quis nostrud exerci tation ullamcorper suscipit lobortis nisl ut aliquip ex ea commodo consequat. Duis autem vel eum iriure dolor in hendrerit in vulputate velit esse molestie cosequat, vel illum dolore eu feugiat. Ut wisi suscipit lobortis nisl ut aliquip tincidunt ut laoreet dolore magna aliquam erat volutpat. Ut wisi enim ad minim veniam, quis nostrud exer. Duis autem vel eum iriure dolor in hendrerit in vulputate elit esse.</p>

  <div class="photo photo-terrace" role="img" aria-label="Photo of a modern home terrace overlooking a lake and mountains"></div>
  <div class="photo photo-house" role="img" aria-label="Photo of a contemporary house with a garden under a blue sky"></div>

  <div class="tab contact-tab">Contact Us</div>
  <ul class="contact-list">
    <li><svg viewBox="0 0 12 12"><path d="M2.5 1 4.5 3.2 3.6 4.6C4.3 6 5.9 7.6 7.4 8.4L8.8 7.5 11 9.5 9.8 11C5.5 10.6 1.4 6.5 1 2.2Z"/></svg>555-410-2836</li>
    <li><svg viewBox="0 0 12 12"><path d="M0 2h12v1.2L6 7 0 3.2Z M0 4.6 6 8.4 12 4.6V10H0Z"/></svg>DanaWhitfield@HarborlineHomes.net</li>
    <li><svg viewBox="0 0 12 12"><path d="M6 .8 12 6H10.3v5H7.3V7.8H4.7V11H1.7V6H0Z"/></svg>218 Coastal Rd, Ste 4 C, Pelican Shores, FL 30112</li>
  </ul>
  <div class="footer-band"></div>
</section>

<section class="card back">
  <div class="title-band"></div>
  <h2 class="title">ABOUT ME</h2>
  <div class="brand-box">
    <div class="brand-mark"></div>
    <div class="brand-name"><span class="big">Harborline</span><span class="small">Real Estate Brokerage</span></div>
  </div>

  <div class="portrait-frame"><div class="portrait" role="img" aria-label="Portrait photo of the broker"></div></div>

  <h3 class="agent-name">DANA M. WHITFIELD</h3>
  <ul class="contact-list">
    <li><svg viewBox="0 0 12 12"><path d="M2.5 1 4.5 3.2 3.6 4.6C4.3 6 5.9 7.6 7.4 8.4L8.8 7.5 11 9.5 9.8 11C5.5 10.6 1.4 6.5 1 2.2Z"/></svg>555-410-7719</li>
    <li><svg viewBox="0 0 12 12"><circle cx="6" cy="6" r="5" fill="none" stroke="#26348a" stroke-width="1.3"/><path d="M1 6h10M6 1v10" stroke="#26348a" stroke-width="1" fill="none"/><ellipse cx="6" cy="6" rx="2.3" ry="5" fill="none" stroke="#26348a" stroke-width="1"/></svg>www.HarborlineHomes.net</li>
    <li><svg viewBox="0 0 12 12"><path d="M0 2h12v1.2L6 7 0 3.2Z M0 4.6 6 8.4 12 4.6V10H0Z"/></svg>DanaWhitfield@HarborlineHomes.net</li>
  </ul>
  <p class="blog-label">Find me on my blog:</p>
  <p class="blog-url">http://coralcountyhomenews.com/blog</p>

  <div class="bio">
    <p>Dana M. Whitfield, Broker and Owner of Harborline Real Estate Brokerage, has had a successful career in Real Estate Management and saless for over 15 years.</p>
    <p>She has served the Coral County Community as the Seaside council of Realtors in every leadership capacity. She has also served as the Coastal Homeowners Outreach Commitee Chairperson.</p>
    <p>Dana has also taught Orientation for new Realtors at the Pelican Bay Association of Realtors and for the youth at Dune Park High School for Young Builders.</p>
    <p>Recently Dana and the Brokerage were choosen by Harbor Home Trust as a preferred vendor for listing and marketing properties acquired through the Harbor Home Trust process</p>
  </div>

  <div class="stamp-box"></div>
  <div class="address-line" style="top:355px"></div>
  <div class="address-line" style="top:387px"></div>
  <div class="address-line" style="top:424px"></div>
</section>

</body>
</html>
```